Modern Minimalistic Supplement Label

Opportunity for recurring projects with a growing company. We have provided a detailed creative brief and all necessary files and guidelines. If you have any questions we will be closely monitoring the discussion board and email provided.

THE NAMES LISTED IN THE BRIEF ARE DIFFERENT FROM THE LABEL TEMPLATES. This is a private label brand. The label templates given are generic so please examine the entire brief before starting.

Use the PSD mockups attached and pair the labels with the correct bottles.

Do not use an entirely white background.

This could be excellent portfolio material.

Start by looking at the "CREATIVE_BRIEF" file. Logo files are contained in the "67046451" zip file.

UPDATE* Use the following business address for the "manufactured for" box on the labels.

Bramwell
4817 Pelton Ave. #2096
Ann Arbor MI 48276

Target Market(s)

All information provided in "CREATIVE_BRIEF" file.

Industry/Entity Type

Supplement

Requirements
Must have
• All information provided in "CREATIVE_BRIEF" file.
Nice to have
Should not have

```html
<!DOCTYPE html>
<html lang="en">
<head>
<meta charset="utf-8">
<title>Bramwell Whey Protein Label</title>
<link rel="stylesheet" href="https://fonts.googleapis.com/css2?family=Oswald:wght@500;600&family=Roboto+Condensed:wght@500;700&display=swap">
<style>
  :root {
    --backdrop: #ecebe8;
    --label-bg: #2b2b2d;
    --copper: #a15d3d;
    --ink-light: #ffffff;
    --rule-grey: #8a8a8c;
  }
  * { margin: 0; padding: 0; box-sizing: border-box; }
  html, body {
    width: 1200px;
    height: 1200px;
    overflow: hidden;
    background: var(--backdrop);
  }
  .canvas {
    position: relative;
    width: 1200px;
    height: 1200px;
  }
  .label {
    position: absolute;
    left: 220px;
    top: 162px;
    width: 760px;
    height: 875px;
    background: var(--label-bg);
    color: var(--ink-light);
    overflow: hidden;
  }
  .brand-name {
    position: absolute;
    top: 86px;
    left: 0;
    width: 100%;
    text-align: center;
    font-family: "Roboto Condensed", sans-serif;
    font-weight: 700;
    font-size: 36px;
    letter-spacing: 7px;
    color: var(--copper);
  }
  .product-title {
    position: absolute;
    left: 172px;
    font-family: "Oswald", sans-serif;
    font-weight: 600;
    line-height: 1;
    text-transform: uppercase;
  }
  .product-title--main {
    top: 188px;
    font-size: 206px;
    letter-spacing: 2px;
  }
  .product-title--sub {
    top: 405px;
    font-size: 92px;
    letter-spacing: 1px;
  }
  .product-variant {
    position: absolute;
    left: 178px;
    top: 557px;
    font-family: "Roboto Condensed", sans-serif;
    font-weight: 500;
    font-size: 33px;
    letter-spacing: 5px;
  }
  .flavor-band {
    position: absolute;
    left: 0;
    top: 621px;
    width: 100%;
    height: 53px;
    background: var(--copper);
  }
  .flavor-name {
    position: absolute;
    left: 178px;
    top: 8px;
    font-family: "Roboto Condensed", sans-serif;
    font-weight: 700;
    font-size: 35px;
    line-height: 1;
    letter-spacing: 6px;
  }
  .flavor-rule {
    position: absolute;
    left: 0;
    top: 685px;
    width: 100%;
    height: 3px;
    background: var(--ink-light);
  }
  .protein-badge {
    position: absolute;
    left: 581px;
    top: 583px;
    width: 114px;
    height: 114px;
    background: var(--label-bg);
    border: 2px solid var(--ink-light);
    display: flex;
    flex-direction: column;
    align-items: center;
    justify-content: center;
    font-family: "Roboto Condensed", sans-serif;
    font-weight: 700;
    line-height: 1.1;
  }
  .protein-badge__amount { font-size: 31px; }
  .protein-badge__unit { font-size: 22px; }
  .benefit {
    position: absolute;
    left: 178px;
    top: 745px;
    font-family: "Roboto Condensed", sans-serif;
    font-weight: 500;
    font-size: 27px;
    letter-spacing: 2px;
  }
  .benefit-rule {
    position: absolute;
    left: 178px;
    top: 790px;
    width: 517px;
    height: 2px;
    background: var(--rule-grey);
  }
  .net-weight {
    position: absolute;
    left: 178px;
    top: 816px;
    font-family: "Roboto Condensed", sans-serif;
    font-weight: 500;
    font-size: 19px;
    letter-spacing: 1px;
  }
</style>
</head>
<body>
<main class="canvas">
  <section class="label">
    <div class="brand-name">BRAMWELL</div>
    <h1 class="product-title product-title--main">Whey</h1>
    <h2 class="product-title product-title--sub">Protein</h2>
    <div class="product-variant">ISOLATE BLEND</div>
    <div class="flavor-band"><span class="flavor-name">CHOCOLATE</span></div>
    <div class="flavor-rule"></div>
    <div class="protein-badge">
      <span class="protein-badge__amount">24G</span>
      <span class="protein-badge__unit">PROTEIN</span>
    </div>
    <p class="benefit">FOR INCREASED MUSCULAR RECOVERY</p>
    <div class="benefit-rule"></div>
    <p class="net-weight">NET WT. 907 G ( 2 LB ) | DIETARY SUPPLEMENT</p>
  </section>
</main>
</body>
</html>
```